Book cover design for the book titled "Quieter Under Lanterns."

create a book cover. The book title is, "Quieter Under Lanterns: A Ledger of Harbour Songs Across Mild Winters." The purpose of the book is to create awareness of how childhood trauma is impacting 7 out of 10 adults in the world today and that two-thirds of children will experience neglect and or abuse before their 18th birthday. One victim described that his mental and physical illness resulting from childhood trauma felt like he wa being pulled to the ground, that the force was "quieter under lanterns." The design should be clean and simple and communicate a crisis.

```html
<!DOCTYPE html>
<html lang="en">
<head>
<meta charset="utf-8">
<title>Quieter Under Lanterns — Book Cover</title>
<link href="https://fonts.googleapis.com/css2?family=Montserrat:wght@400;600;700&display=swap" rel="stylesheet">
<style>
  :root {
    --backdrop: #414043;
    --cover: #e6e6e6;
    --ink: #0b0b0b;
    --ink-soft: #1c1c1c;
    --figure-light: #f4f4f4;
    --figure-mid: #dcdcdc;
  }
  * { margin: 0; padding: 0; box-sizing: border-box; }
  html, body {
    width: 1200px;
    height: 727px;
    overflow: hidden;
    background: var(--backdrop);
    font-family: "Montserrat", sans-serif;
  }
  .canvas {
    position: relative;
    width: 1200px;
    height: 727px;
    display: flex;
    align-items: center;
    justify-content: center;
  }
  .cover {
    position: relative;
    width: 510px;
    height: 660px;
    background: var(--cover);
    box-shadow: 0 10px 24px rgba(0,0,0,0.45);
    overflow: hidden;
  }
  .cover-figure {
    position: absolute;
    left: 170px;
    top: 30px;
    width: 250px;
    height: 560px;
    border-radius: 45% 55% 40% 50% / 30% 30% 60% 60%;
    background: radial-gradient(ellipse at 50% 35%, var(--figure-light) 0%, var(--figure-mid) 55%, rgba(230,230,230,0) 75%);
    opacity: 0.7;
  }
  .title {
    position: absolute;
    left: 0;
    right: 0;
    top: 58px;
    padding-left: 28px;
    color: var(--ink);
    text-shadow: 4px 6px 6px rgba(0,0,0,0.28);
  }
  .title-lead {
    display: block;
    font-weight: 600;
    font-size: 37px;
    line-height: 1;
    letter-spacing: -0.5px;
  }
  .title-main {
    display: block;
    font-weight: 700;
    font-size: 77px;
    line-height: 0.95;
    letter-spacing: -1px;
    margin-top: 4px;
  }
  .subtitle {
    position: absolute;
    left: 0;
    right: 0;
    top: 198px;
    text-align: center;
    font-weight: 700;
    font-size: 12.5px;
    letter-spacing: 2.6px;
    color: var(--ink);
  }
  .blurb {
    position: absolute;
    left: 30px;
    right: 30px;
    top: 526px;
    text-align: center;
    font-weight: 400;
    font-size: 9.4px;
    line-height: 13.4px;
    color: var(--ink-soft);
  }
  .byline {
    position: absolute;
    left: 0;
    right: 0;
    top: 600px;
    text-align: center;
    font-weight: 700;
    font-size: 19px;
    color: var(--ink);
  }
</style>
</head>
<body>
  <main class="canvas">
    <article class="cover">
      <div class="cover-figure" role="img" aria-label="Faint pale photograph of a crouching figure bowed over, arms wrapped around the head"></div>
      <h1 class="title">
        <span class="title-lead">QUIETER UNDER</span>
        <span class="title-main">LANTERNS</span>
      </h1>
      <p class="subtitle">CHILDHOOD TRAUMA DESTROYS HUMANITY</p>
      <p class="blurb">The purpose of the book is to create awareness of how childhood trauma is impacting 7 out of 10 adults in the world today and that two-thirds of children will experience neglect and or abuse before their 18th birthday. One victim described that his mental and physical illness resulting from childhood trauma felt like he wa being pulled to the ground, that the force was "quieter under lanterns.</p>
      <p class="byline">By. you name</p>
    </article>
  </main>
</body>
</html>
```